Wow me with your Earring card options!

An A7 portrait sized earring card is required for Velvet & Vinyl. Inspired by Velvet and fueled by Vinyl we love our accessories to do the talking. Bold statement earrings are our thing. Our earring cards need to showcase our brand while not stealing all of the limelight from the earrings themselves. Earring care information needs to be included on the back side of the card. Our simple logo needs to be the basis for the colour choices used on the card.

Need extra days to review

• No florals please 😊

```html
<!DOCTYPE html>
<html lang="en">
<head>
<meta charset="utf-8">
<title>Velvet &amp; Vinyl – Earring Card</title>
<link rel="stylesheet" href="https://fonts.googleapis.com/css2?family=Poppins:wght@700&family=Quicksand:wght@500&family=Caveat&display=swap">
<style>
  :root {
    --frame: #22a09f;
    --ink: #08090b;
    --paper: #ffffff;
    --grey: #a9a9a9;
    --tile-1: #08090b;
    --tile-2: #d9252b;
    --tile-3: #1f5fa8;
    --tile-4: #e5478f;
  }
  * { margin: 0; padding: 0; box-sizing: border-box; }
  html, body { width: 1200px; height: 827px; overflow: hidden; background: var(--paper); }
  .sheet { position: relative; width: 1200px; height: 827px; }

  .card { position: absolute; top: 84px; width: 466px; height: 661px; padding: 11px; background: var(--frame); }
  .card--front { left: 107px; }
  .card--back { left: 629px; }
  .card__face { position: relative; width: 100%; height: 100%; }
  .card--front .card__face { background: var(--ink); }
  .card--back .card__face { background: var(--paper); }

  .brand-name {
    position: absolute; top: 262px; left: 0; right: 0; text-align: center;
    font-family: "Poppins", sans-serif; font-weight: 700; font-size: 50px;
    color: var(--paper);
  }
  .hang-hole { position: absolute; top: 557px; width: 10px; height: 10px; border-radius: 50%; background: var(--paper); }
  .hang-hole--left { left: 148px; }
  .hang-hole--right { left: 295px; }

  .care-title {
    position: absolute; top: 66px; left: 77px;
    font-family: "Poppins", sans-serif; font-weight: 700; font-size: 58px; line-height: 1;
    color: var(--ink);
  }
  .care-subtitle {
    position: absolute; top: 118px; left: 118px; transform: rotate(-5deg);
    font-family: "Caveat", cursive; font-size: 44px; color: var(--grey);
  }

  .care-list { position: absolute; top: 188px; left: 52px; list-style: none; }
  .care-list li { display: flex; align-items: center; height: 36.5px; font-family: "Quicksand", sans-serif; font-size: 16px; color: var(--ink); }
  .care-list svg { width: 34px; height: 30px; margin-right: 10px; flex: none; }

  .contact-list { position: absolute; top: 341px; left: 82px; list-style: none; }
  .contact-list li { display: flex; align-items: center; height: 31px; font-family: "Quicksand", sans-serif; font-size: 15.5px; color: var(--ink); }
  .contact-icon { width: 28px; height: 28px; margin-right: 18px; flex: none; }

  .social-row { position: absolute; top: 451px; left: 250px; display: flex; gap: 8px; }
  .social-row span { width: 24px; height: 24px; border-radius: 3px; }
  .social-row .s1 { background: var(--tile-1); }
  .social-row .s2 { background: var(--tile-2); }
  .social-row .s3 { background: var(--tile-3); }
  .social-row .s4 { background: var(--tile-4); }
</style>
</head>
<body>
<main class="sheet">
  <section class="card card--front">
    <div class="card__face">
      <p class="brand-name">Velvet &amp; Vinyl</p>
      <span class="hang-hole hang-hole--left"></span>
      <span class="hang-hole hang-hole--right"></span>
    </div>
  </section>

  <section class="card card--back">
    <div class="card__face">
      <h1 class="care-title">EARRING</h1>
      <p class="care-subtitle">Care instructions</p>

      <ul class="care-list">
        <li><svg viewBox="0 0 34 30" fill="none" stroke="#08090b" stroke-width="1.3"><path d="M12 8 C8 14 5 18 5 22 a7 7 0 0 0 14 0 c0-4-3-8-7-14z"/><path d="M24 2 c-2 3-3 5-3 6.5 a3 3 0 0 0 6 0 c0-1.5-1-3.5-3-6.5z"/></svg>Avoid moisture &amp; remove before bathing</li>
        <li><svg viewBox="0 0 34 30" fill="none" stroke="#08090b" stroke-width="1.5"><rect x="5" y="3" width="24" height="13" rx="1"/><rect x="8" y="8" width="7" height="5"/><rect x="19" y="8" width="7" height="5"/><path d="M5 16 L2 21 H32 L29 16 M2 21 V27 H32 V21 M4 27 v2 M30 27 v2"/></svg>For comforts sake, remove before bed!</li>
        <li><svg viewBox="0 0 34 30" fill="none" stroke="#08090b" stroke-width="1.3"><rect x="12" y="11" width="9" height="18" rx="2"/><rect x="14" y="5" width="5" height="6"/><path d="M23 4 h2 M23 7 h3 M23 2 h2"/></svg>Avoid contact with perfumes &amp; lotions</li>
        <li><svg viewBox="0 0 34 30" fill="none" stroke="#08090b" stroke-width="1.3"><circle cx="17" cy="15" r="8"/><path d="M17 1v3 M17 26v3 M3 15h3 M28 15h3 M7 5l2 2 M25 23l2 2 M7 25l2-2 M25 7l2-2"/></svg>Store away from direct sunlight</li>
      </ul>

      <ul class="contact-list">
        <li><svg class="contact-icon" viewBox="0 0 30 30"><circle cx="15" cy="15" r="15" fill="#08090b"/><g fill="none" stroke="#fff" stroke-width="1.3"><circle cx="15" cy="15" r="8"/><ellipse cx="15" cy="15" rx="3.5" ry="8"/><path d="M7 15h16"/></g></svg>www.velvetandvinyl.com.au</li>
        <li><svg class="contact-icon" viewBox="0 0 30 30"><circle cx="15" cy="15" r="15" fill="#08090b"/><g fill="none" stroke="#fff" stroke-width="1.3"><rect x="7" y="9.5" width="16" height="11"/><path d="M7 9.5 L15 16 L23 9.5"/></g></svg>hello@velvetandvinyl.com.au</li>
        <li><svg class="contact-icon" viewBox="0 0 30 30"><circle cx="15" cy="15" r="15" fill="#08090b"/><g fill="none" stroke="#fff" stroke-width="1.3"><circle cx="17" cy="11" r="3.5"/><path d="M10 22 q7-9 14 0 M6 16h5 M8.5 13.5v5"/></g></svg>@velvetandvinyl</li>
      </ul>

      <div class="social-row" role="img" aria-label="Social media links">
        <span class="s1"></span><span class="s2"></span><span class="s3"></span><span class="s4"></span>
      </div>
    </div>
  </section>
</main>
</body>
</html>
```